Modern, upmarket label design for food product

We need a label design for a food company producing nuts with sesame and honey. In fact, we would like the words "Cashews med sesam & honning" on the label (It's in Danish and means - Cashews with sesame & honey). It should be easy for the customer to quickly understand what it is.

It is a shelf product in the competitive food industry, which is why the design should wake the feeling of 'just wanting to grab the product down from the shelves'. So, the design should stand out and have an image of a cool, modern, hip product. This being said, I love a raw & handmade look.

The company is called Tyvo. Its origins are from the danish word Pilt that is a Danish slang for yummy. I have uploaded a photo of the package the products will be sold in.

Info & dimensions on bag in picture 1.
Dimensions: 6" x 9" | 15.2 cm x 22.3 cm
Capacity: 8 ounces | 250 grams (based on whole bean coffee)

Picture 2 is the same product, but has the possibility of attaching to a hanger on shelfs.

Picture 3 - I have also uploaded a photo of a product bag, where the hole is linear instead of a round hole. The designer chooses, which bag they will like to work with!

Please let me know if there are any questions!

Target Market(s)

Target market could really be any age, but the design needs to compel the target audience to pick it from the shelves. The package should signal a product you want to hold and have other people seeing you have it. The target audience is people who cares for what they buy, and typically doesn't want a low-end or budget product. They want the whole thing, meaning it has to taste good, look good etc. They are also the type of people who like to show off whatever products they buy by placing them in their houses for their guests to see. Or by uploading pictures of it on social medias.

Industry/Entity Type

It Company

Font styles to use
Other font styles liked:
• Not a must, but I like the 'Panton' script

Requirements
Must have
• My project must have the words 'Cashews med sesam & honning' on the label, so the customer will know within a second what they are looking at and buying.
Nice to have
• I am picturing the label with the words 'Cashews med sesam & honning' as a statement, again, emphasizing how the customer instantly should know what the product is. This being said, it should not be the only thing on the package and I love a raw & handmade look - which inspiration picture 5 is a great example of!
• I have uploaded photos of what I think looks good. With this said, I am not looking for a copy of those products, but see them as good inspiration. I have named the photos inspiration 1, 2, 3, 4 & 5.
• If needed, more text can be put on the label. For example 'vegan', 'laktosefri', Glutenfri', or 'Sund Snack' are great words for being used on the label.
Should not have
• The fonts on the label should not be too decorative. Personally I like an easy too read font.

```html
<!DOCTYPE html>
<html lang="da">
<head>
<meta charset="utf-8">
<title>Tyvo – cashews med sesam &amp; honning</title>
<link rel="stylesheet" href="https://fonts.googleapis.com/css2?family=Jost:wght@300;400;500&display=swap">
<style>
  :root {
    --page: #ffffff;
    --kraft: #bf9779;
    --window: #ede1db;
    --cream: #ffffff;
    --ink: #231f20;
    --shadow: rgba(0, 0, 0, 0.28);
  }
  html, body {
    margin: 0;
    padding: 0;
    width: 915px;
    height: 1200px;
    overflow: hidden;
    background: var(--page);
  }
  .label {
    display: block;
    width: 915px;
    height: 1200px;
  }
  .label-face {
    fill: var(--kraft);
    filter: drop-shadow(1px 2px 2px var(--shadow));
  }
  .seal-line { stroke: var(--cream); stroke-width: 1.2; }
  .bar { fill: var(--cream); }
  .bar-dark { fill: var(--ink); }
  .window { fill: var(--window); }
  .title {
    font-family: "Jost", "Futura", sans-serif;
    font-weight: 300;
    font-size: 96px;
    fill: var(--cream);
  }
  .ampersand {
    font-family: "Jost", "Futura", sans-serif;
    font-weight: 300;
    font-size: 70px;
    fill: var(--ink);
  }
  .brand {
    font-family: "Jost", "Futura", sans-serif;
    font-weight: 500;
    font-size: 34px;
    fill: var(--cream);
  }
  .weight {
    font-family: "Jost", "Futura", sans-serif;
    font-weight: 400;
    font-size: 22px;
    fill: var(--cream);
  }
  .divider { stroke: var(--ink); stroke-width: 2; }
</style>
</head>
<body>
<svg class="label" viewBox="0 0 915 1200" xmlns="http://www.w3.org/2000/svg" role="img" aria-label="Tyvo cashews med sesam og honning, 8 ounces, 250 grams">
  <rect class="label-face" x="137" y="120" width="641" height="940"/>

  <line class="seal-line" x1="137" y1="210" x2="792" y2="210"/>

  <g class="vertical-bars">
    <rect class="bar" x="190" y="120" width="13" height="940"/>
    <rect class="bar" x="237" y="120" width="12" height="422"/>
    <rect class="bar" x="285" y="120" width="12" height="472"/>
  </g>

  <g class="product-name">
    <text class="title" x="318" y="395" textLength="332" lengthAdjust="spacingAndGlyphs">cashews</text>
    <text class="title" x="505" y="447" textLength="163" lengthAdjust="spacingAndGlyphs">med</text>
    <text class="title" x="348" y="500" textLength="222" lengthAdjust="spacingAndGlyphs">sesam</text>
    <text class="ampersand" x="568" y="541">&amp;</text>
    <text class="title" x="330" y="585" textLength="290" lengthAdjust="spacingAndGlyphs">honning</text>
  </g>

  <ellipse class="window" cx="456" cy="764" rx="210" ry="125"/>

  <g class="side-stripes">
    <rect class="bar-dark" x="702" y="770" width="76" height="12"/>
    <rect class="bar" x="702" y="797" width="76" height="13"/>
    <rect class="bar-dark" x="702" y="826" width="76" height="13"/>
  </g>

  <text class="brand" x="457" y="967" text-anchor="middle">Tyvo</text>
  <text class="weight" x="434" y="1007" text-anchor="end">8 ounces</text>
  <line class="divider" x1="450" y1="984" x2="450" y2="1017"/>
  <text class="weight" x="466" y="1007">250 grams</text>
</svg>
</body>
</html>
```